We also do Plumbing Reminder! Our Primary Color is Green with Gold accent.

We are a HVAC, plumbing, and Controls contractor based out of West Michigan, Serving the entire west side of the state.
We want to remind our customers we do plumbing. Customers don't know or remember that we do plumbing. We would like the final design to show images, and descriptions of plumbing services we offer.

Lift Stations
Sinks
Confined Space
Backflow Prevention Devices​ (testing, installation, & service)
Drinking Fountains
Roof Drains
Sump Pumps
Water Main Emergency Service
Toilets / Urinals
Faucets / Shower Valves
Piping​ (copper, PVC, steel, PEX, galvanized)
Water Heaters
Floor and Sink Drains
​NEW INSTALLATIONS, SERVICE, AND MAINTENANCE OF ALL BRANDS OF EQUIPMENT

```html
<!DOCTYPE html>
<html lang="en">
<head>
<meta charset="utf-8">
<title>Halden Mechanical – Plumbing Services Flyer</title>
<link href="https://fonts.googleapis.com/css2?family=Audiowide&family=Montserrat:wght@500;600;700;800&display=swap" rel="stylesheet">
<style>
  :root{
    --bg:#dcdcdc;
    --paper:#ffffff;
    --green:#12905c;
    --green-dark:#0b6a43;
    --gold:#c9a04a;
    --gold-light:#e2c274;
    --gold-dark:#a67c2b;
    --ink:#1d2f26;
    --photo-sand:#a88a62;
    --photo-wall:#8d8f8c;
    --photo-brass:#9a8a66;
  }
  *{box-sizing:border-box;margin:0;padding:0}
  html,body{width:1200px;height:3770px;overflow:hidden;background:var(--bg)}
  body{position:relative;font-family:"Montserrat",sans-serif;color:var(--ink)}
  .flyer{position:absolute;left:60px;top:1121px;width:1080px;height:1527px;background:var(--paper);box-shadow:0 6px 24px rgba(0,0,0,.18);overflow:hidden}
  .header-art{position:absolute;left:0;top:0;width:1080px;height:740px}
  .brand{position:absolute;left:635px;top:48px;width:445px;text-align:center;font-weight:800;color:var(--green);font-size:44px;line-height:1.05;letter-spacing:1px}
  .services-title{position:absolute;left:112px;top:768px;width:860px;height:86px;border-radius:20px;background:linear-gradient(90deg,var(--gold-dark),var(--gold-light) 50%,var(--gold-dark));color:#fff;font-family:"Audiowide",sans-serif;font-size:44px;display:flex;align-items:center;justify-content:center;letter-spacing:1px}
  .service{position:absolute;display:flex;align-items:center;gap:26px}
  .service svg{width:70px;height:70px;flex:none;fill:none;stroke:var(--green);stroke-width:3;stroke-linecap:round;stroke-linejoin:round}
  .service .label{font-weight:500;font-size:25px;line-height:1.05}
  .service .note{display:block;font-size:11px;margin-top:6px;font-weight:500}
  .service .note.wide{font-size:15px}
  .tagline{position:absolute;left:422px;top:1306px;color:var(--green);font-weight:800;font-size:22px;line-height:1.2}
  .footer{position:absolute;left:0;top:1430px;width:1080px;height:72px}
  .footer svg{position:absolute;left:0;top:0}
  .footer .web{position:absolute;left:68px;top:18px;color:#fff;font-weight:700;font-size:28px}
  .footer .phone{position:absolute;right:40px;top:14px;color:#fff;font-weight:700;font-size:34px}
</style>
</head>
<body>
<main class="flyer">
  <svg class="header-art" viewBox="0 0 1080 740">
    <defs>
      <linearGradient id="goldGrad" x1="0" x2="1" y1="0" y2="1">
        <stop offset="0" stop-color="#a67c2b"/><stop offset=".5" stop-color="#e6c67a"/><stop offset="1" stop-color="#a67c2b"/>
      </linearGradient>
      <linearGradient id="sand" x1="0" y1="0" x2="0" y2="1">
        <stop offset="0" stop-color="#c9c6bd"/><stop offset=".35" stop-color="#a88a62"/><stop offset="1" stop-color="#8a6d47"/>
      </linearGradient>
    </defs>
    <rect x="635" y="212" width="445" height="246" fill="#8d8f8c" role="img" aria-label="Photo of commercial water heaters with white piping"/>
    <rect x="560" y="464" width="520" height="240" fill="#9a8a66" role="img" aria-label="Photo of brass backflow prevention valves on a pipe line"/>
    <path d="M0 0 H600 C660 180 650 420 560 560 C470 690 300 725 0 722 Z" fill="none" stroke="url(#goldGrad)" stroke-width="24"/>
    <path d="M0 0 H600 C660 180 650 420 560 560 C470 690 300 725 0 722 Z" fill="url(#sand)" role="img" aria-label="Photo of a plumber laying PVC pipe in an excavated floor trench"/>
  </svg>
  <div class="brand">HALDEN<br>MECHANICAL</div>

  <div class="services-title">PLUMBING SERVICES WE OFFER</div>

  <div class="service" style="left:96px;top:885px"><svg viewBox="0 0 70 70"><rect x="12" y="30" width="46" height="28"/><path d="M24 30V16h22v14M35 16V8M28 8h14"/></svg><span class="label">Lift<br>Stations</span></div>
  <div class="service" style="left:96px;top:985px"><svg viewBox="0 0 70 70"><circle cx="35" cy="38" r="14"/><path d="M8 38h13M49 38h13M35 24V12M27 12h16"/></svg><span class="label">Backflow<br>Prevention<br>Devices<span class="note">(Testing, Installation &amp; Service)</span></span></div>
  <div class="service" style="left:96px;top:1096px"><svg viewBox="0 0 70 70"><path d="M8 36h54l-6 20H14z"/><path d="M20 36V18a6 6 0 0 1 12 0"/><circle cx="40" cy="14" r="3"/></svg><span class="label">Drinking<br>Fountains</span></div>
  <div class="service" style="left:96px;top:1200px"><svg viewBox="0 0 70 70"><path d="M8 38h54l-6 18H14z"/><path d="M16 38V14h12M28 14v8"/><path d="M26 26l-4 6M30 26v6M34 26l4 6"/></svg><span class="label">Faucets /<br>Shower<br>Valves</span></div>
  <div class="service" style="left:96px;top:1302px"><svg viewBox="0 0 70 70"><circle cx="35" cy="35" r="26"/><circle cx="35" cy="35" r="18"/><path d="M23 35h24M35 23v24M27 27l16 16M43 27L27 43"/></svg><span class="label">Floor and<br>Sink Drains</span></div>

  <div class="service" style="left:418px;top:888px"><svg viewBox="0 0 70 70"><path d="M8 26h54v8a27 27 0 0 1-54 0z"/><path d="M35 26V10M27 10h16M35 56v10"/></svg><span class="label">Sinks</span></div>
  <div class="service" style="left:418px;top:990px"><svg viewBox="0 0 70 70"><rect x="12" y="12" width="46" height="46"/><rect x="20" y="20" width="30" height="30"/><path d="M20 28h30M20 35h30M20 42h30"/></svg><span class="label">Roof<br>Drains</span></div>
  <div class="service" style="left:418px;top:1096px"><svg viewBox="0 0 70 70"><path d="M14 18h30v12h-8v8"/><path d="M20 12h12M26 12v6"/><path d="M36 46c-4 6-4 10 0 12s4-6 0-12z"/></svg><span class="label">Water Main<br>Emergency<br>Service</span></div>
  <div class="service" style="left:418px;top:1198px"><svg viewBox="0 0 70 70"><path d="M14 12h22a10 10 0 0 1 0 20H24a10 10 0 0 0 0 20h22"/><path d="M46 46v12M14 6v12"/></svg><span class="label">Piping<span class="note wide">(Copper, PVC, steel, PEX,<br>Galvanized)</span></span></div>

  <div class="service" style="left:784px;top:885px"><svg viewBox="0 0 70 70"><circle cx="35" cy="35" r="26"/><circle cx="35" cy="35" r="16"/><circle cx="35" cy="14" r="2"/><circle cx="35" cy="56" r="2"/><circle cx="14" cy="35" r="2"/><circle cx="56" cy="35" r="2"/></svg><span class="label">Confined<br>Space</span></div>
  <div class="service" style="left:784px;top:990px"><svg viewBox="0 0 70 70"><rect x="14" y="22" width="42" height="36" rx="6"/><path d="M28 22V10h14v12M22 58v6M48 58v6"/><circle cx="35" cy="40" r="6"/></svg><span class="label">Sump<br>Pumps</span></div>
  <div class="service" style="left:784px;top:1096px"><svg viewBox="0 0 70 70"><rect x="18" y="8" width="34" height="14" rx="3"/><path d="M14 28h42c0 14-8 20-21 20S14 42 14 28zM26 48l-2 14h22l-2-14"/></svg><span class="label">Toilets /<br>Urinals</span></div>
  <div class="service" style="left:784px;top:1198px"><svg viewBox="0 0 70 70"><rect x="18" y="10" width="34" height="48" rx="8"/><circle cx="35" cy="36" r="8"/><path d="M35 36l3-4M28 58v6M42 58v6"/></svg><span class="label">Water<br>Heaters</span></div>

  <p class="tagline">NEW INSTALLATIONS SERVICE AND<br>MAINTENANCE OF ALL BRANDS OF EQUIPMENT</p>

  <div class="footer">
    <svg width="1080" height="72" viewBox="0 0 1080 72">
      <defs><linearGradient id="goldBand" x1="0" x2="1"><stop offset="0" stop-color="#a67c2b"/><stop offset=".5" stop-color="#e2c274"/><stop offset="1" stop-color="#b88d38"/></linearGradient></defs>
      <polygon points="0,0 620,0 580,72 0,72" fill="var(--green)"/>
      <polygon points="620,0 1080,0 1080,72 580,72" fill="url(#goldBand)"/>
    </svg>
    <span class="web">www.haldenmechanical.com</span>
    <span class="phone">1-800-555-0142</span>
  </div>
</main>
</body>
</html>
```